Präsentationsvorlagen für Unternehmensberater
Zielgruppe
Ich bin selbstständiger Unternehmensberater / Freelancer / Projektmanager / Interimmanager und Trainer in den Bereichen operative Logistik und Logistik-IT. Meine Kundenmix reicht vom Kleinunternehmen bis hin zu multinationalen Konzernen. Meine Projekte führen mich nach ganz Europa, mit Schwerpunkten im Osten. Als Projektsprachen verwende ich deutsch und englisch.
Aufgabenstellung
Ich suche nach einem umfangreichen Powerpoint-Masterfile zur Verwendung sowohl in der Aquisitionsphase als auch in den Projekten. Das moderne Design muss am Corporate Design angelehnt sein (siehe beiliegende Dateien, Webpage ist noch in Entwicklung, die aktuelle Layoutplanung ist aber verfügbar und kann bei Bedarf übermittelt werden). Geschwungene Formen bevorzuge ich gegenüber gradliniger Geometrie. Ein wenig verspielt darf es sein, ohne jedoch an Professionalität einzubüßen.
Folgendes soll im Masterfile berücksichtigt werden:
Aufbau:
- Dreistufige Struktur (Titel / Bereich / Thema)
- verborgene Folien / direkter Klick auf Themen z.B. von Inhaltsverzeichnis werden genutzt
- Animationen werden verwendet
- Seitenverhältnis 16:9
aktuell geplante Folientypen (Vorlage für alle Typen gewünscht):
- Agenda
- Übersicht / Inhalt
- Text/Aufzählung
- Zeitleiste
- Bilder mit/ohne Textspalte
- eingebundenes Video mit/ohne Text
- Darstellung ineinandergreifender Themen (ähnlich Puzzle)
- Diagramme (Kreisdiagramm, Balkendiagramm, Liniendiagramm, Spiderweb) jeweils mit und ohne Textspalte
- Gegenüberstellungen (z.B. Vor- und Nachteile)
- Wordcloud
- Prozessschritte
- Flowcharts
- Tabellen
- magisches Dreick/Vieleck (Darstellung untereinander konkurrierenden Ziele)
- Slogans / Zitate / Hypothesen
- Mengenüberschneidungen
- Call to Action
- Schlussfolie / Fragen?
- Kontaktdaten

```html
<!DOCTYPE html>
<html lang="de">
<head>
<meta charset="utf-8">
<title>Agenda – Folienvarianten</title>
<link rel="stylesheet" href="https://fonts.googleapis.com/css2?family=Lato:wght@400;700;900&display=swap">
<style>
  :root{
    --stage:#dedede;
    --slide:#ffffff;
    --brand-blue:#27a9e1;
    --accent-cyan:#00c3f5;
    --accent-blue:#139fd9;
    --neutral-grey:#a6a6a6;
    --heading:#333333;
    --body:#777777;
    --footer-grey:#9a9a9a;
  }
  *{margin:0;padding:0;box-sizing:border-box}
  html,body{width:708px;height:1200px;overflow:hidden;background:var(--stage)}
  body{position:relative;font-family:"Lato",Arial,sans-serif}
  .slide-frame{position:absolute;left:34.6px;width:638px;height:359px;overflow:hidden}
  .slide{position:absolute;left:0;top:0;width:1198px;height:674px;background:var(--slide);
    transform:scale(0.53255);transform-origin:0 0;overflow:hidden}
  .slide svg.shapes{position:absolute;left:0;top:0;width:1198px;height:674px}
  .header-wave,.footer-wave{fill:var(--brand-blue)}
  .slide-title{position:absolute;left:46px;top:18px;font-size:35px;font-weight:900;color:#fff;letter-spacing:-0.3px}
  .slide-date{position:absolute;left:46px;top:76px;font-size:15px;color:#fff;letter-spacing:6.5px}
  .slide-date.inline{left:353px;top:48px}
  .brand{position:absolute;right:18px;top:28px;display:flex;align-items:center;gap:6px;
    font-size:17px;font-weight:700;color:var(--brand-blue)}
  .brand-dot{width:14px;height:14px;border-radius:50%;background:var(--neutral-grey)}
  .agenda-item{position:absolute;width:440px;height:90px}
  .agenda-item .num{position:absolute;left:0;top:7px;width:76px;height:76px;border-radius:50%;
    display:flex;align-items:center;justify-content:center;color:#fff;font-size:21px;font-weight:700}
  .agenda-item .item-title{position:absolute;left:89px;top:0;font-size:21px;font-weight:700;color:var(--heading);white-space:nowrap}
  .agenda-item .item-text{position:absolute;left:89px;top:31px;font-size:13.5px;line-height:19px;color:var(--body);white-space:nowrap}
  .num.cyan{background:var(--accent-cyan)}
  .num.blue{background:var(--accent-blue)}
  .num.grey{background:var(--neutral-grey)}
  .active-frame{position:absolute;left:127px;top:317px;width:455px;height:89px;border:3px solid var(--accent-blue);border-radius:45px}
  .page-no{position:absolute;left:21px;top:643px;font-size:14px;color:#fff;letter-spacing:5px}
  .site{position:absolute;right:23px;top:637px;font-size:13px;color:#fff;letter-spacing:6px}
  .plain-footer .page-no,.plain-footer .site{color:var(--footer-grey)}
</style>
</head>
<body>

<!-- Variante 1 -->
<div class="slide-frame" style="top:35.2px">
  <section class="slide">
    <svg class="shapes" viewBox="0 0 1198 674">
      <path class="header-wave" d="M0,0 H568 C545,20 540,50 540,80 V110 C540,140 505,146 445,144 C370,141 280,118 190,118 C100,118 30,127 0,133 Z"/>
      <path class="footer-wave" d="M0,614 C100,636 200,643 300,640 C500,634 750,570 970,571 C1080,572 1150,582 1198,593 V674 H0 Z"/>
    </svg>
    <h1 class="slide-title">Agenda</h1>
    <p class="slide-date">01/02/2020</p>
    <div class="brand"><span class="brand-dot"></span>velnora</div>
    <div class="active-frame"></div>
    <div class="agenda-item" style="left:135px;top:192px"><span class="num cyan">01</span><h2 class="item-title">Subtitle demo text</h2><p class="item-text">Lorem ipsum dolor sed do sit amet, consectetur<br>adipiscing elit, sed do eiusmod tempor sed re eu</p></div>
    <div class="agenda-item" style="left:134px;top:317px"><span class="num blue">02</span><h2 class="item-title">Subtitle demo text</h2><p class="item-text">Lorem ipsum dolor sed do sit amet, consectetur<br>adipiscing elit, sed do eiusmod tempor sed re eu</p></div>
    <div class="agenda-item" style="left:135px;top:442px"><span class="num grey">03</span><h2 class="item-title">Subtitle demo text</h2><p class="item-text">Lorem ipsum dolor sed do sit amet, consectetur<br>adipiscing elit, sed do eiusmod tempor sed re eu</p></div>
    <div class="agenda-item" style="left:624px;top:192px"><span class="num grey">04</span><h2 class="item-title">Subtitle demo text</h2><p class="item-text">Lorem ipsum dolor sed do sit amet, consectetur<br>adipiscing elit, sed do eiusmod tempor sed re eu</p></div>
    <div class="agenda-item" style="left:622px;top:317px"><span class="num blue">05</span><h2 class="item-title">Subtitle demo text</h2><p class="item-text">Lorem ipsum dolor sed do sit amet, consectetur<br>adipiscing elit, sed do eiusmod tempor sed re eu</p></div>
    <div class="agenda-item" style="left:624px;top:442px"><span class="num cyan">06</span><h2 class="item-title">Subtitle demo text</h2><p class="item-text">Lorem ipsum dolor sed do sit amet, consectetur<br>adipiscing elit, sed do eiusmod tempor sed re eu</p></div>
    <span class="page-no">02</span>
    <span class="site">www.velnora.at</span>
  </section>
</div>

<!-- Variante 2 -->
<div class="slide-frame" style="top:420.8px">
  <section class="slide">
    <svg class="shapes" viewBox="0 0 1198 674">
      <path class="header-wave" d="M0,0 H568 C545,20 540,50 540,80 V110 C540,140 505,146 445,144 C370,141 280,118 190,118 C100,118 30,127 0,133 Z"/>
      <path class="footer-wave" d="M0,614 C100,636 200,643 300,640 C500,634 750,570 970,571 C1080,572 1150,582 1198,593 V674 H0 Z"/>
    </svg>
    <h1 class="slide-title">Agenda</h1>
    <p class="slide-date inline">01/02/2020</p>
    <div class="brand"><span class="brand-dot"></span>velnora</div>
    <div class="active-frame"></div>
    <div class="agenda-item" style="left:135px;top:192px"><span class="num cyan">01</span><h2 class="item-title">Subtitle demo text</h2><p class="item-text">Lorem ipsum dolor sed do sit amet, consectetur<br>adipiscing elit, sed do eiusmod tempor sed re eu</p></div>
    <div class="agenda-item" style="left:134px;top:317px"><span class="num blue">02</span><h2 class="item-title">Subtitle demo text</h2><p class="item-text">Lorem ipsum dolor sed do sit amet, consectetur<br>adipiscing elit, sed do eiusmod tempor sed re eu</p></div>
    <div class="agenda-item" style="left:135px;top:442px"><span class="num grey">03</span><h2 class="item-title">Subtitle demo text</h2><p class="item-text">Lorem ipsum dolor sed do sit amet, consectetur<br>adipiscing elit, sed do eiusmod tempor sed re eu</p></div>
    <div class="agenda-item" style="left:624px;top:192px"><span class="num grey">04</span><h2 class="item-title">Subtitle demo text</h2><p class="item-text">Lorem ipsum dolor sed do sit amet, consectetur<br>adipiscing elit, sed do eiusmod tempor sed re eu</p></div>
    <div class="agenda-item" style="left:622px;top:317px"><span class="num blue">05</span><h2 class="item-title">Subtitle demo text</h2><p class="item-text">Lorem ipsum dolor sed do sit amet, consectetur<br>adipiscing elit, sed do eiusmod tempor sed re eu</p></div>
    <div class="agenda-item" style="left:624px;top:442px"><span class="num cyan">06</span><h2 class="item-title">Subtitle demo text</h2><p class="item-text">Lorem ipsum dolor sed do sit amet, consectetur<br>adipiscing elit, sed do eiusmod tempor sed re eu</p></div>
    <span class="page-no">02</span>
    <span class="site">www.velnora.at</span>
  </section>
</div>

<!-- Variante 3 -->
<div class="slide-frame" style="top:806.5px">
  <section class="slide plain-footer">
    <svg class="shapes" viewBox="0 0 1198 674">
      <path class="header-wave" d="M0,0 H568 C545,20 540,50 540,80 V110 C540,140 505,146 445,144 C370,141 280,118 190,118 C100,118 30,127 0,133 Z"/>
    </svg>
    <h1 class="slide-title">Agenda</h1>
    <p class="slide-date">01/02/2020</p>
    <div class="brand"><span class="brand-dot"></span>velnora</div>
    <div class="active-frame"></div>
    <div class="agenda-item" style="left:135px;top:192px"><span class="num cyan">01</span><h2 class="item-title">Subtitle demo text</h2><p class="item-text">Lorem ipsum dolor sed do sit amet, consectetur<br>adipiscing elit, sed do eiusmod tempor sed re eu</p></div>
    <div class="agenda-item" style="left:134px;top:317px"><span class="num blue">02</span><h2 class="item-title">Subtitle demo text</h2><p class="item-text">Lorem ipsum dolor sed do sit amet, consectetur<br>adipiscing elit, sed do eiusmod tempor sed re eu</p></div>
    <div class="agenda-item" style="left:135px;top:442px"><span class="num grey">03</span><h2 class="item-title">Subtitle demo text</h2><p class="item-text">Lorem ipsum dolor sed do sit amet, consectetur<br>adipiscing elit, sed do eiusmod tempor sed re eu</p></div>
    <div class="agenda-item" style="left:624px;top:192px"><span class="num grey">04</span><h2 class="item-title">Subtitle demo text</h2><p class="item-text">Lorem ipsum dolor sed do sit amet, consectetur<br>adipiscing elit, sed do eiusmod tempor sed re eu</p></div>
    <div class="agenda-item" style="left:622px;top:317px"><span class="num blue">05</span><h2 class="item-title">Subtitle demo text</h2><p class="item-text">Lorem ipsum dolor sed do sit amet, consectetur<br>adipiscing elit, sed do eiusmod tempor sed re eu</p></div>
    <div class="agenda-item" style="left:624px;top:442px"><span class="num cyan">06</span><h2 class="item-title">Subtitle demo text</h2><p class="item-text">Lorem ipsum dolor sed do sit amet, consectetur<br>adipiscing elit, sed do eiusmod tempor sed re eu</p></div>
    <span class="page-no">02</span>
    <span class="site">www.velnora.at</span>
  </section>
</div>

</body>
</html>
```